Mend Your Frame
Stationary
Project: Mend Your Frame
Mend Your Frame - Health
Creative Brief
Use specific fonts
Whatever fonts look best!
Professional
Dellan Corvin
Body Composition Specialist/ Personal Trainer
Dont put address.
dellcorvin@mailnest.example
MendYourFrameAnalysis.example
We use a state of the art body composition analyzer to accurately determine total body fat, essential fat, non essential fat, reserve fat, total body water, and lean mass. It's fast, non-invasive, and comparable to the Gold Standard. To find out more visit our website or call us.

```html
<!DOCTYPE html>
<html lang="en">
<head>
<meta charset="utf-8">
<title>Mend Your Frame – Business Card</title>
<link rel="stylesheet" href="https://fonts.googleapis.com/css2?family=Open+Sans:wght@400;600;700;800&display=swap">
<style>
  :root {
    --backdrop: #2b2b2d;
    --card: #ffffff;
    --brand-blue: #1f6fc4;
    --brand-blue-light: #4a9ae0;
    --ink: #4a4a4a;
    --ink-soft: #6d6d6d;
    --rule: #9a9a9a;
    --swoosh-grey: #a9adb2;
    --swoosh-grey-dark: #7d8288;
  }
  * { box-sizing: border-box; margin: 0; padding: 0; }
  html, body { width: 1200px; height: 780px; overflow: hidden; }
  body {
    background: var(--backdrop);
    font-family: "Open Sans", Arial, sans-serif;
    position: relative;
  }
  .business-card {
    position: absolute;
    left: 75px;
    top: 90px;
    width: 1050px;
    height: 600px;
    background: var(--card);
    border-radius: 34px;
    overflow: hidden;
    box-shadow: 0 18px 40px rgba(0,0,0,.45);
  }
  .brand {
    position: absolute;
    left: 170px;
    top: 130px;
    width: 600px;
  }
  .brand-name {
    font-weight: 800;
    font-size: 78px;
    line-height: 0.98;
    letter-spacing: -1px;
    color: var(--brand-blue);
    text-transform: uppercase;
  }
  .person {
    position: absolute;
    right: 620px;
    top: 365px;
    text-align: right;
  }
  .person-name {
    font-weight: 700;
    font-size: 40px;
    color: var(--brand-blue);
    letter-spacing: -0.5px;
    line-height: 1.1;
  }
  .person-role {
    font-weight: 600;
    font-size: 20px;
    color: var(--ink-soft);
    line-height: 1.35;
  }
  .divider {
    position: absolute;
    left: 450px;
    top: 350px;
    width: 3px;
    height: 130px;
    background: var(--rule);
  }
  .contact-list {
    position: absolute;
    left: 475px;
    top: 352px;
    list-style: none;
  }
  .contact-item {
    display: flex;
    align-items: center;
    gap: 14px;
    font-size: 22px;
    color: var(--ink);
    height: 43px;
  }
  .contact-icon { width: 24px; height: 24px; flex: none; }
  .card-swoosh {
    position: absolute;
    left: 0;
    bottom: 0;
    width: 1050px;
    height: 150px;
  }
</style>
</head>
<body>
  <main class="business-card">
    <header class="brand">
      <div class="brand-name">Mend Your<br>Frame</div>
    </header>

    <section class="person">
      <h1 class="person-name">Dellan Corvin</h1>
      <p class="person-role">Body Composition Specialist</p>
      <p class="person-role">Personal Trainer</p>
    </section>

    <div class="divider"></div>

    <ul class="contact-list">
      <li class="contact-item">
        <svg class="contact-icon" viewBox="0 0 24 24" aria-hidden="true">
          <path d="M6.6 3.5c.6-.3 1.2 0 1.5.5l1.7 3.2c.3.6.1 1.2-.4 1.6L8 9.8c.9 2.3 3.1 4.6 5.6 5.8l1.1-1.4c.4-.5 1.1-.6 1.6-.3l3.1 1.8c.5.3.7 1 .4 1.5l-1 2c-.4.8-1.3 1.2-2.2 1-7.2-1.6-11.8-7-12.7-13.4-.1-.9.4-1.8 1.2-2.2z" fill="var(--brand-blue)"/>
        </svg>
        <span>555.014.2290</span>
      </li>
      <li class="contact-item">
        <svg class="contact-icon" viewBox="0 0 24 24" aria-hidden="true">
          <circle cx="12" cy="12" r="4.2" fill="none" stroke="var(--brand-blue)" stroke-width="2.6"/>
          <path d="M16.2 8v5.5c0 1.6 2.8 2 3.6-.2A8.5 8.5 0 1 0 16 19.6" fill="none" stroke="var(--brand-blue)" stroke-width="2.6" stroke-linecap="round"/>
        </svg>
        <span>dellcorvin@mailnest.example</span>
      </li>
      <li class="contact-item">
        <svg class="contact-icon" viewBox="0 0 24 24" aria-hidden="true">
          <circle cx="12" cy="12" r="10" fill="none" stroke="var(--brand-blue)" stroke-width="2"/>
          <ellipse cx="12" cy="12" rx="4.5" ry="10" fill="none" stroke="var(--brand-blue)" stroke-width="1.6"/>
          <path d="M2 12h20M4 7h16M4 17h16" stroke="var(--brand-blue)" stroke-width="1.6"/>
        </svg>
        <span>www.MendYourFrameAnalysis.example</span>
      </li>
    </ul>

    <svg class="card-swoosh" viewBox="0 0 1050 150" preserveAspectRatio="none" aria-hidden="true">
      <defs>
        <linearGradient id="swooshGrey" x1="0" y1="0" x2="1" y2="0">
          <stop offset="0" stop-color="var(--swoosh-grey-dark)"/>
          <stop offset="0.5" stop-color="var(--swoosh-grey)"/>
          <stop offset="1" stop-color="var(--swoosh-grey-dark)"/>
        </linearGradient>
        <linearGradient id="swooshBlue" x1="0" y1="0" x2="1" y2="0">
          <stop offset="0" stop-color="var(--brand-blue)"/>
          <stop offset="0.55" stop-color="var(--brand-blue-light)"/>
          <stop offset="1" stop-color="var(--brand-blue)"/>
        </linearGradient>
      </defs>
      <path d="M0 40 C 260 150, 640 150, 1050 20 L1050 150 L0 150 Z" fill="url(#swooshGrey)"/>
      <path d="M0 95 C 300 150, 700 110, 1050 30 L1050 150 L0 150 Z" fill="url(#swooshBlue)"/>
    </svg>
  </main>
</body>
</html>
```